Wine labels Velmora Wine Council - Nueva etiqueta El Consejo Regulador de vinos de Albarrán

Velmora Wines Council, based in southern Spain, are looking to create a new suite of wine labels which retain the elegance of the Velmora Wines industry while reinvigorating their image to the modern era and a new generation of Sherry Wine lovers. These labels will be used across the Velmora Wines Council's range of wines for the promotion of the Velmora Wines industry.

Your design must present at least two styles of Velmora Wines which demonstrate an elegant, modern interpretation and understanding of the unique mood and personality for these wines and the essence of southern Spain.

10 labels will be created based on the winning design, one for each of the unique varieties of Velmora Wines within the collection. This collection comprises of several different wine varieties including: Fino, Manzanilla, Amontillado, Oloroso, Palo Cortado, Medium, Cream, Pale Cream, Pedro Ximenez and Moscatel.

We recommend you visit our website www.velmora-vinos.example/wines as the source to understanding the origins and unique personality of these diverse wines.

El Consejo Regulador de los Vinos de Albarrán y Tordesal quiere renovar las etiquetas de los vinos utilizados para sus actividades de promoción genérica. Esta colección de vinos comprende las tipologías más importantes de la región que incluye: fino, manzanilla, amontillado, oloroso, palo cortado, pale cream, medium, cream, pedro ximénez y moscatel. Por lo tanto se precisan 10 etiquetas, una para cada uno de los vinos mencionados.
Updates

Project Deadline Extended
Reason: Due to some confusion with the deadline we wish to officially extend the deadline to allow designers one last week to submit their entries.

Target Market(s)

Industry, journalists, media, sommeliers, chefs, wine writers

Industry/Entity Type

Council

Requirements
Must have
• Front and Back label plus capsule:
• Front label can have either of the two official logos of the Velmora Wine council titled Vinos de Albarrán Digital or not, this is optional. Must include: Vino selecionado por el Consejo Regulador de la Denominacion de Origen, Name of the variety of wine eg FINO, percentage of alcohol eg 15% and quantity 75 cl.
• The back of the label must include the council logo titled Sellora and 4 additional logos positioned smaller. The Europa logo must appear larger than the 3 other logos. Space for descriptive text about the wine is also required.
• The dimensions of the bottle can be found at this link http://www.vidrialto.example/es/catalogo/vinos-y-espumosos/bordelesas/bd-orla
• Altura:305 mm
• Diámetro base:76,20 mm
• Diámetro hombro:82 mm
• Tipo boca:Cetie
• Peso:750 gr
• Capacidad:75 cl
• Etiqueta delantera y trasera y capsula
• La etiqueta delantera puede incluir el logo oficial del Consejo Regulador o el logo digital, o ninguno, esto es opcional. Debe incluir el siguiete texto: Vino selecionado por el Consejo Regulador de la Denominacion de Origen, el nombre de la variedad del vino, por ejemplo Fino, el porcentaje de alcohol, por ejemplo 15%, y la capacidad 75cl.
• La etiqueta trasera debe incluir el logo oficial Sellora del Consejo, y cuatro logos adicionales con una dimension menor. El Logo de ¨Europa invierte en las zonas rurales¨ debe ser de mayor tamaño que los otros. Se precisa espacio para el texto descriptivo de los vinos.
• Las dimensiones de la botella se puede encontrar en este enlace
• http://www.vidrialto.example/es/catalogo/vinos-y-espumosos/bordelesas/bd-orla
• Altura:305 mm
• Diámetro base:76,20 mm
• Diámetro hombro:82 mm
• Tipo boca:Cetie
• Peso:750 gr
• Capacidad:75 cl
Nice to have
• See our website velmora-vinos.example to understand the origin of the wines. Ver nuestra página web velmora-vinos.example para mejor entender los vinos.
Should not have
• Images of catavinos or stereotypical images from Spain such as flamenco dancers or guitars.

```html
<!DOCTYPE html>
<html lang="es">
<head>
<meta charset="utf-8">
<title>Velmora Wine Council – Etiquetas Manzanilla y Fino</title>
<link href="https://fonts.googleapis.com/css2?family=PT+Sans:wght@400;700&family=Ubuntu:wght@400&display=swap" rel="stylesheet">
<style>
  :root {
    --backdrop: #f3ece1;
    --label-black: #1b1b1b;
    --capsule-black: #141414;
    --ink-light: #e9e6df;
    --manzanilla-gold: #e3a52a;
    --manzanilla-base: #6e5a2c;
    --fino-gold: #f1d43b;
    --fino-base: #5e5a26;
  }
  * { margin: 0; padding: 0; box-sizing: border-box; }
  html, body {
    width: 1200px; height: 906px; overflow: hidden;
    background: var(--backdrop);
  }
  .collection {
    position: relative; width: 1200px; height: 906px;
  }
  .wine { position: absolute; top: 70px; width: 300px; }
  .wine--manzanilla { left: 203px; --accent: var(--manzanilla-gold); --base: var(--manzanilla-base); }
  .wine--fino { left: 679px; --accent: var(--fino-gold); --base: var(--fino-base); }

  .capsule {
    width: 110px; height: 120px; margin: 0 auto 40px;
    background: var(--capsule-black);
    border-radius: 6px 6px 2px 2px;
    display: flex; flex-direction: column; align-items: center; justify-content: center;
    gap: 4px;
  }
  .capsule .brand-name { font-size: 9px; color: var(--accent); }
  .capsule .brand-sub { font-size: 5px; color: var(--accent); }

  .front-label {
    height: 600px;
    background: linear-gradient(to bottom, var(--label-black) 0%, var(--label-black) 62%, var(--base) 100%);
    display: flex; flex-direction: column; align-items: center;
    padding-top: 46px;
    color: var(--ink-light);
    font-family: "PT Sans", sans-serif;
  }
  .brand { display: flex; flex-direction: column; align-items: center; gap: 6px; }
  .brand-mark {
    width: 14px; height: 14px; border-radius: 50%;
    background: var(--ink-light); margin-bottom: 8px;
  }
  .brand-name {
    font-family: "PT Sans", sans-serif; font-weight: 400;
    font-size: 16px; letter-spacing: 0.5px; text-transform: uppercase;
  }
  .brand-sub {
    font-family: "PT Sans", sans-serif; font-weight: 400;
    font-size: 7px; letter-spacing: 2.5px; text-transform: uppercase;
  }
  .grape-art {
    margin-top: 30px; width: 170px; height: 200px;
  }
  .vintage { margin-top: 30px; font-size: 10px; letter-spacing: 3px; }
  .variety {
    margin-top: 14px;
    font-family: "Ubuntu", sans-serif; font-weight: 400;
    color: var(--accent); line-height: 1;
  }
  .wine--manzanilla .variety { font-size: 33px; }
  .wine--fino .variety { font-size: 48px; margin-top: 8px; }
  .certification {
    margin-top: 40px; text-align: center;
    font-size: 9.5px; line-height: 1.2; color: var(--ink-light);
  }
  .certification strong { display: block; font-size: 11px; font-weight: 700; }
  .specs {
    margin-top: 12px; display: flex; align-items: center; gap: 8px;
    font-size: 8.5px;
  }
  .specs .divider { width: 1px; height: 16px; background: var(--ink-light); }
</style>
</head>
<body>
<main class="collection">

  <article class="wine wine--manzanilla">
    <div class="capsule">
      <span class="brand-name">Vinos de Albarrán</span>
      <span class="brand-sub">Velmora Wines</span>
    </div>
    <section class="front-label">
      <div class="brand">
        <span class="brand-mark"></span>
        <span class="brand-name">Vinos de Albarrán</span>
        <span class="brand-sub">Velmora Wines</span>
      </div>
      <svg class="grape-art" viewBox="0 0 170 200" role="img" aria-label="Racimo de uvas dibujado con espirales doradas bajo una hoja de parra">
        <defs>
          <radialGradient id="manzanilla-glow" cx="50%" cy="50%" r="55%">
            <stop offset="0%" stop-color="#e3a52a" stop-opacity="0.55"/>
            <stop offset="100%" stop-color="#e3a52a" stop-opacity="0"/>
          </radialGradient>
        </defs>
        <rect width="170" height="200" fill="url(#manzanilla-glow)"/>
      </svg>
      <div class="vintage">2016</div>
      <h2 class="variety">MANZANILLA</h2>
      <p class="certification">Vino seleccionado por el
        <strong>Consejo Regulador</strong>
        de la Denominación de Origen</p>
      <div class="specs"><span>75cl</span><span class="divider"></span><span>alc 15%</span></div>
    </section>
  </article>

  <article class="wine wine--fino">
    <div class="capsule">
      <span class="brand-name">Vinos de Albarrán</span>
      <span class="brand-sub">Velmora Wines</span>
    </div>
    <section class="front-label">
      <div class="brand">
        <span class="brand-mark"></span>
        <span class="brand-name">Vinos de Albarrán</span>
        <span class="brand-sub">Velmora Wines</span>
      </div>
      <svg class="grape-art" viewBox="0 0 170 200" role="img" aria-label="Racimo de uvas trazado con líneas curvas amarillas bajo una hoja de parra">
        <defs>
          <radialGradient id="fino-glow" cx="50%" cy="50%" r="55%">
            <stop offset="0%" stop-color="#f1d43b" stop-opacity="0.55"/>
            <stop offset="100%" stop-color="#f1d43b" stop-opacity="0"/>
          </radialGradient>
        </defs>
        <rect width="170" height="200" fill="url(#fino-glow)"/>
      </svg>
      <div class="vintage">2016</div>
      <h2 class="variety">FINO</h2>
      <p class="certification">Vino seleccionado por el
        <strong>Consejo Regulador</strong>
        de la Denominación de Origen</p>
      <div class="specs"><span>75cl</span><span class="divider"></span><span>alc 15%</span></div>
    </section>
  </article>

</main>
</body>
</html>
```